Electrical company needs a brochure designed for electrical construction work

we need a brochure designed for our company BRONZEPATH ELECTRICAL INSTALLATIONS. we are a group of electricians working in the construction industry delivering electrical constructon services to builders and other clients in the commercial and Industrial working environments. we would like our logo to stand out with a dark theme and also give a professional fee.l we have a brief description of what we do and our experiences in a word doc i will provide it along with our logo design

Target Market(s)

builders for commercial and industrial construction projects

Industry/Entity Type

Electric Company

Font styles to use
Serif

Colors
0456a4
96b7d9
5c5c5c
757575
000000
aaaaaa
ec1f27
33a6d7
0493ce

Requirements
Must have
• a professional feel,
Nice to have
• some wording that makes us stand out and brings all the attention

```html
<!DOCTYPE html>
<html lang="en">
<head>
<meta charset="utf-8">
<title>Bronzepath Electrical Installations – Brochure</title>
<link href="https://fonts.googleapis.com/css2?family=Montserrat:wght@300;400;600;700&display=swap" rel="stylesheet">
<style>
  :root{
    --navy:#0456a4; --sky:#96b7d9; --grey-dark:#5c5c5c; --grey:#757575;
    --black:#000000; --grey-light:#aaaaaa; --red:#ec1f27; --cyan:#33a6d7;
    --blue:#0493ce; --paper:#ffffff; --stage:#efefef; --ink:#3a3a3a;
    --cover:#141414; --cover-band:#1b1b1b;
  }
  *{box-sizing:border-box;margin:0;padding:0}
  html,body{width:902px;height:1200px;overflow:hidden;background:var(--stage)}
  body{position:relative;font-family:"Montserrat",Arial,sans-serif;color:var(--ink)}
  .spread{position:absolute;left:75px;width:753px;height:486px;overflow:hidden}
  .spread svg{position:absolute;inset:0}
  .spread-outside{top:58px;background:var(--cover)}
  .spread-inside{top:611px;background:var(--paper)}

  /* outside */
  .faint-name{position:absolute;left:-150px;top:200px;transform:rotate(-90deg);
    font:700 62px "Montserrat",sans-serif;color:#1e1e1e;letter-spacing:2px;white-space:nowrap}
  .faint-sub{position:absolute;left:-40px;top:200px;transform:rotate(-90deg);
    font:400 17px "Montserrat",sans-serif;color:#222;letter-spacing:6px;white-space:nowrap}
  .contact{position:absolute;left:118px;top:421px;width:140px;text-align:center;color:#ddd;
    font-size:6.6px;line-height:10px}
  .contact .contact-name{color:var(--red);font-size:9.5px;line-height:12px;text-transform:uppercase}
  .brand{position:absolute;display:flex;align-items:center;gap:7px}
  .brand .brand-dot{width:26px;height:26px;border-radius:50%;background:var(--blue);flex:none}
  .brand .brand-name{font-weight:700;color:var(--blue);line-height:1.15;letter-spacing:.5px}
  .brand-cover{left:430px;top:250px}
  .brand-cover .brand-name{font-size:17px}
  .web{position:absolute;font-size:7.5px;letter-spacing:2.5px;color:#9a9a9a}
  .web-cover{left:506px;top:456px}

  /* inside left */
  .about{position:absolute;left:21px;top:160px;color:#fff}
  .about .kicker{font:400 13px "Montserrat",sans-serif;color:#e5e5e5}
  .about .headline{font:700 20px/22px "Montserrat",sans-serif;color:var(--blue)}
  .brand-inside{left:212px;top:22px}
  .brand-inside .brand-dot{width:18px;height:18px}
  .brand-inside .brand-name{font-size:10px}
  .body-copy{position:absolute;left:21px;top:297px;width:336px;font-size:5.5px;line-height:7.8px;
    color:var(--grey-dark);text-align:justify}
  .body-copy p{margin-bottom:6px}
  .web-inside{left:21px;top:455px;color:var(--grey-dark);font-size:6.5px}

  /* inside right */
  .intro,.closing{position:absolute;left:409px;width:314px;font-size:6.6px;line-height:9.5px;
    color:var(--grey-dark);text-align:justify}
  .intro{top:22px}
  .closing{top:234px}
  .quote-mark{position:absolute;font:700 16px Georgia,serif;color:#c9c9c9}
  .projects{position:absolute;left:419px;top:98px;width:300px;display:grid;
    grid-template-columns:1fr 1fr;grid-auto-rows:15px;column-gap:12px;list-style:none}
  .projects li{position:relative;padding:1px 0 0 11px;border-bottom:1px solid #ececec;
    font-size:5.6px;line-height:6.5px;font-weight:600;color:#333;overflow:hidden}
  .projects li::before{content:"";position:absolute;left:0;top:2px;width:4px;height:4px;
    border:1px solid var(--red);border-radius:50%}
  .signoff{position:absolute;left:476px;top:312px;width:160px;text-align:center}
  .signoff .thanks{font-size:6px;color:var(--grey)}
  .signoff .signer{font-size:10px;font-weight:700;color:var(--navy);margin-top:6px;text-transform:uppercase}
  .promo{position:absolute;right:15px;top:366px;width:150px;text-align:right;color:#fff}
  .promo .promo-lead{font-size:11px;color:var(--blue);line-height:13px}
  .promo .promo-title{font-size:12px;font-weight:700;line-height:14px}
  .promo .promo-text{font-size:5.4px;line-height:7px;color:#ddd;margin-top:4px}
</style>
</head>
<body>

<section class="spread spread-outside" aria-label="Brochure outside">
  <svg width="753" height="486" viewBox="0 0 753 486">
    <rect width="753" height="486" fill="var(--cover)"/>
    <rect x="0" y="0" width="376" height="486" fill="var(--cover-band)"/>
    <rect role="img" aria-label="Faint world map texture" x="120" y="40" width="620" height="420" fill="#181818" opacity=".6"/>
  </svg>
  <div class="faint-name">BRONZEPATH</div>
  <div class="faint-sub">ELECTRICAL INSTALLATIONS</div>
  <div class="contact">
    <div class="contact-name">Daniel Whitcombe</div>
    <div>Bronzepath Electrical Installations</div>
    <div>0400555218</div>
    <div>hello@bronzepath.com.au</div>
  </div>
  <div class="brand brand-cover">
    <span class="brand-dot"></span>
    <span class="brand-name">BRONZEPATH<br>ELECTRICAL INSTALLATIONS</span>
  </div>
  <div class="web web-cover">www.bronzepath.au</div>
</section>

<section class="spread spread-inside" aria-label="Brochure inside">
  <svg width="753" height="486" viewBox="0 0 753 486">
    <defs>
      <linearGradient id="photoWork" x1="0" y1="0" x2="1" y2="1">
        <stop offset="0" stop-color="#d8d8d8"/><stop offset=".5" stop-color="#8a9aa8"/><stop offset="1" stop-color="#3c5f80"/>
      </linearGradient>
      <linearGradient id="photoCity" x1="0" y1="0" x2="1" y2="1">
        <stop offset="0" stop-color="#f2b35a"/><stop offset=".5" stop-color="#b87035"/><stop offset="1" stop-color="#3b2a22"/>
      </linearGradient>
    </defs>
    <polygon role="img" aria-label="Photo collage of an electrician wiring a switchboard" points="3,40 45,0 175,0 300,70 377,80 377,230 300,270 230,250 180,275 0,282 0,60" fill="url(#photoWork)"/>
    <polygon points="0,105 150,150 240,225 0,282" fill="#2b2b2b"/>
    <polygon role="img" aria-label="Photo of a city skyline at sunset" points="377,300 470,345 753,345 753,486 377,486" fill="url(#photoCity)"/>
    <polygon points="753,275 540,385 753,486" fill="#2e2e2e"/>
    <polygon points="753,330 600,420 753,486" fill="#1f1f1f" opacity=".6"/>
  </svg>

  <div class="brand brand-inside">
    <span class="brand-dot"></span>
    <span class="brand-name">BRONZEPATH<br>ELECTRICAL INSTALLATIONS</span>
  </div>
  <div class="about">
    <div class="kicker">ABOUT</div>
    <div class="headline">OUR<br>COMPANY</div>
  </div>
  <div class="body-copy">
    <p>Electrical contracting company able to perform a great variety of electrical work required, recent experience on heavy industrial electrical installs involving complex systems on gas plant, 5 years total. Commercial and industrial situations are something we have always been exposed to and have been involved in many large construction jobs around Portmere.</p>
    <p>We are a small company just getting started and have been operating part time for over a year working late nights after our day jobs, working most weekends Saturday and Sundays, working towards building our company to be able to work full time and grow our business to something we can be proud of.</p>
    <p>Recently the opportunity arose that we could move away from our employment and take the business to a new level and work full time with 100% commitment we believe that our drive and passion for our trade and industry separates us from the unwilling and we will push ourselves to the limit to achieve and exceed any expectations that are placed upon us.</p>
    <p>Our background in large commercial and industrial construction jobs around Portmere has granted us the ability to introduce and implement stringent safety practices, we will always encourage and drive safety to the best of our ability to mitigate risk or harm to any person, not just because of our duty of care but because we like to see potential work colleagues/employees go home safely to their families unharmed.</p>
  </div>
  <div class="web web-inside">www.bronzepath.au</div>

  <span class="quote-mark" style="left:396px;top:16px">&ldquo;</span>
  <p class="intro">I'm Daniel Whitcombe a local electrician in Portmere running a small electrical contracting company Bronzepath Electrical Installations. If you are in need of reliable, punctual, and experienced electricians to work in with your company then please give me a call I'm happy to discuss my business or submit a quote for any work you may have available. I have a lot of experience in the local construction industry I have worked on a lot of commercial and industrial construction jobs around Portmere for at least the last 10 years some jobs include.</p>
  <ul class="projects">
    <li>Northgate high school</li><li>Eastfield barracks single leap project</li>
    <li>St Brigid's college</li><li>Civic chambers multiple contracts</li>
    <li>Underground cabling on many subdivisions including Hillcrest, Oakvale, Redmere</li><li>The Portmere convention centre</li>
    <li>Stationhouse retail</li><li>Airbase runway lighting</li>
    <li>Eastbank substation HV switch gear</li><li>Portmere airport multiple different contracts</li>
    <li>Westhill substation HV switch gear</li><li>Portmere hospital oncology building</li>
    <li>The Portmere harbourside wave pool etc</li><li>Portmere hospital multiple various maintenance contracts</li>
    <li>Sandy bay receiving station project</li><li>Portmere correctional facility</li>
  </ul>
  <span class="quote-mark" style="left:396px;top:228px">&ldquo;</span>
  <p class="closing">This list is not every job I have worked on but it gives a clear picture of what work I can perform as an electrical contractor. Most of the listed jobs I worked in a leadership role as either a leading hand or supervisor so I have been involved in construction meetings and meeting deadlines and working in with other contractors to achieve the best results for all parties involved. I'm trying to keep it short and sweet but if you decide to go with Bronzepath electrical installations to do your electrical work you will not regret it. I pride myself on my quality of work, work ethics and my prices are competitive.</p>
  <div class="signoff">
    <div class="thanks">Thank you very much for taking the time.</div>
    <div class="signer">Daniel Whitcombe</div>
  </div>
  <div class="promo">
    <div class="promo-lead">Lorem IpSum Is</div>
    <div class="promo-title">Simply Dummy Text</div>
    <div class="promo-text">Lorem Ipsum is simply dummy text of the printing and typesetting industry. Lorem Ipsum has been the industry's standard dummy text ever since the 1500s,</div>
  </div>
</section>

</body>
</html>
```